Recruitment Site Design

We need a design for the login page, about page, and inner pages of a recruitment site for an oil and gas company. Design should be modern, sleek, professional and colors can be blue, green, white, orange or any other recommended colors.

Please also take into consideration that once the users login, they will need to access a form to fill in their information.

** UPDATE: Kindly provide a design for the inner information page consistent with the outer design. Attached is a picture of the basic structure. ***
Updates

Please provide a design for inner pages as shown in the design brief consistent with the registration page provided. 

Reason: We're extending it to get more inside pages.

Target Market(s)

Professionals looking for a career in the oil and gas industry in the Middle East.

Industry/Entity Type

Oil And Gas

Requirements
Must have
• Sleek design

```html
<!DOCTYPE html>
<html lang="en">
<head>
<meta charset="utf-8">
<title>Crestline Careers – Basic Information</title>
<link href="https://fonts.googleapis.com/css2?family=Arimo:wght@400;700&display=swap" rel="stylesheet">
<style>
:root{
  --page-top:#dedede;
  --page-mid:#f3f3f3;
  --card:#ffffff;
  --ink:#333333;
  --ink-soft:#555555;
  --brand-blue:#2458b8;
  --nav-top:#3a7ad6;
  --nav-bottom:#1446a6;
  --nav-line:#5d92e0;
  --panel-bg:#f0f0f0;
  --panel-line:#d2d2d2;
  --label-bg:#e4e4e4;
  --field-line:#c4c4c4;
  --footer-top:#5a5a5a;
  --footer-bottom:#8a8a8a;
  --footer-text:#ffffff;
  --accent-red:#d42a1e;
  --accent-gold:#d6a100;
  --accent-navy:#1a4f9c;
  --accent-green:#3c9a3a;
  --accent-deep:#1f3d7a;
  --accent-teal:#1f7a4a;
}
*{box-sizing:border-box;margin:0;padding:0}
html,body{width:1200px;height:944px;overflow:hidden}
body{
  position:relative;font-family:"Arimo",Arial,sans-serif;color:var(--ink);
  background:linear-gradient(var(--page-top) 0,#e9e9e9 252px,var(--page-mid) 253px,var(--page-mid) 847px);
}
.footer-band{position:absolute;left:0;top:847px;width:1200px;height:97px;
  background:linear-gradient(var(--footer-top),var(--footer-bottom))}
.top-links{position:absolute;top:14px;right:195px;font-size:13px;color:var(--ink-soft);display:flex;gap:14px}
.top-links span.sep{color:#777}
.card{position:absolute;left:163px;top:50px;width:877px;height:817px;background:var(--card);
  border-radius:6px;box-shadow:0 4px 14px rgba(0,0,0,.35)}
.brand{position:absolute;left:189px;top:78px}
.brand-name{font-size:40px;font-weight:700;color:var(--brand-blue);letter-spacing:-.5px;line-height:1}
.brand-slogan{font-size:13px;color:var(--ink-soft);margin-top:10px;margin-left:14px}
.date{position:absolute;right:189px;top:145px;font-size:11px;color:var(--ink)}
.main-nav{position:absolute;left:173px;top:170px;width:856px;height:42px;border-radius:3px;
  background:linear-gradient(var(--nav-top),var(--nav-bottom));display:flex;align-items:center}
.main-nav a{color:#fff;text-decoration:none;font-size:11px;height:42px;line-height:42px;padding:0 14px;
  border-right:1px solid var(--nav-line)}
.main-nav a:first-child{padding:0 13px}
.search{position:absolute;right:18px;top:7px;width:170px;height:27px;background:#fff;border-radius:4px;
  font-size:11px;font-style:italic;color:#666;line-height:27px;padding-left:10px}
.search svg{position:absolute;right:5px;top:3px}
.panel{position:absolute;background:var(--panel-bg);border:1px solid var(--panel-line);border-radius:3px}
.panel-head{height:28px;line-height:28px;padding-left:10px;font-size:12px;color:var(--ink);
  background:linear-gradient(#f7f7f7,#dcdcdc);border-bottom:1px solid var(--panel-line)}
.basic-info{left:173px;top:226px;width:639px;height:458px}
.form-row{position:absolute;left:7px;width:624px}
.form-label{position:absolute;left:0;top:0;width:296px;height:100%;background:var(--label-bg);
  font-size:12px;text-align:right;padding:6px 26px 0 0}
.form-label.req::after{content:"*";position:absolute;right:10px;top:7px;font-size:12px}
.field{position:absolute;height:21px;background:#fff;border:1px solid var(--field-line);font-size:11px;padding:4px 6px}
.select::after{content:"";position:absolute;right:0;top:0;width:18px;height:19px;border-left:1px solid var(--field-line);
  background:linear-gradient(#fff,#eee)}
.select svg{position:absolute;right:5px;top:7px;z-index:1}
.mini{position:absolute;font-size:8px;color:var(--ink)}
.small{position:absolute;font-size:11px}
.btn-update{position:absolute;left:323px;top:425px;width:90px;height:24px;border:1px solid #b8b8b8;border-radius:3px;
  background:linear-gradient(#fff,#e2e2e2);font-size:11px;text-align:center;line-height:22px}
.member{left:824px;top:226px;width:204px;height:388px}
.member .panel-head{height:32px;line-height:32px}
.member .panel-head svg{position:absolute;right:14px;top:9px}
.member-list{list-style:none}
.member-list li{height:35px;line-height:35px;font-size:11px;padding-left:28px;position:relative;border-bottom:1px solid #d8d8d8}
.member-list li:last-child{border-bottom:none}
.member-list li::before{content:"";position:absolute;left:12px;top:14px;border-left:5px solid #333;
  border-top:4px solid transparent;border-bottom:4px solid transparent}
.employers{left:173px;top:697px;width:639px;height:152px;background:#fff}
.employers .panel-head{height:35px;line-height:35px;background:linear-gradient(#f7f7f7,#d8d8d8)}
.arrow{position:absolute;top:68px;width:22px;height:58px;border:1px solid #ccc;background:linear-gradient(#fafafa,#dcdcdc)}
.arrow.prev{left:8px;border-radius:8px 0 0 8px}
.arrow.next{right:8px;border-radius:0 8px 8px 0}
.arrow svg{position:absolute;left:5px;top:21px}
.employer-track{position:absolute;left:38px;right:38px;top:68px;height:58px;
  display:flex;align-items:center;justify-content:space-between;padding:0 4px}
.employer{font-weight:700;font-size:15px;display:flex;align-items:center;gap:5px;white-space:nowrap}
.employer .dot{width:13px;height:13px;border-radius:50%}
.employer.northfield{color:var(--accent-red)}
.employer.harborline{color:var(--accent-gold)}
.employer.harborline .dot{background:#e8b800}
.employer.ridgeway{color:var(--accent-navy)}
.employer.greenpoint{color:var(--accent-green)}
.employer.greenpoint .dot{background:#5cb338}
.employer.summit{color:var(--accent-deep)}
.employer.aztera{color:var(--accent-teal)}
.footer-links{position:absolute;top:876px;left:0;width:1200px;display:flex;justify-content:center;gap:14px;
  font-size:11px;color:var(--footer-text)}
.copyright{position:absolute;top:918px;width:1200px;text-align:center;font-size:11px;color:var(--footer-text)}
</style>
</head>
<body>
<div class="footer-band"></div>

<nav class="top-links"><span>Login</span><span class="sep">|</span><span>Register</span><span class="sep">|</span><span>Contact Us</span></nav>

<div class="card"></div>

<header class="brand">
  <div class="brand-name">Crestline Careers</div>
  <div class="brand-slogan">The slogan of your will be here</div>
</header>
<div class="date">Wednesday, 7th November, 2012</div>

<nav class="main-nav">
  <a>HOME</a><a>ABOUT US</a><a>SEARCH JOBS</a><a>CANDIDATES</a><a>RECRUITERS</a><a>FAQ'S</a><a>BLOGS</a><a>ADVICE</a>
  <div class="search">Search
    <svg width="24" height="20" viewBox="0 0 24 20"><circle cx="9" cy="8" r="6" fill="none" stroke="#2458b8" stroke-width="2.5"/><line x1="13.5" y1="12" x2="21" y2="18" stroke="#2458b8" stroke-width="3.5" stroke-linecap="round"/></svg>
  </div>
</nav>

<section class="panel basic-info">
  <div class="panel-head">Basic Information</div>
  <div class="form-row" style="top:42px;height:25px"><div class="form-label req">Firts Name</div><div class="field" style="left:304px;top:2px;width:199px"></div></div>
  <div class="form-row" style="top:72px;height:25px"><div class="form-label req">Last Name</div><div class="field" style="left:304px;top:2px;width:199px"></div></div>
  <div class="form-row" style="top:102px;height:25px"><div class="form-label req">Date of Birth</div><div class="field" style="left:304px;top:2px;width:166px"></div></div>
  <div class="form-row" style="top:132px;height:25px"><div class="form-label req">Place of Birth</div><div class="field" style="left:304px;top:2px;width:199px"></div></div>
  <div class="form-row" style="top:162px;height:25px"><div class="form-label req">Street</div><div class="field" style="left:304px;top:2px;width:199px"></div></div>
  <div class="form-row" style="top:192px;height:25px"><div class="form-label req">City</div><div class="field" style="left:304px;top:2px;width:199px"></div></div>
  <div class="form-row" style="top:222px;height:53px"><div class="form-label req">State</div>
    <span class="small" style="left:306px;top:6px">US</span>
    <div class="field select" style="left:373px;top:2px;width:140px">Selected State<svg width="8" height="5"><path d="M0 0h8L4 5z" fill="#333"/></svg></div>
    <span class="small" style="left:306px;top:32px">Non US</span>
    <div class="field" style="left:373px;top:28px;width:167px">Australia</div>
  </div>
  <div class="form-row" style="top:279px;height:25px"><div class="form-label req">Zip/Postal Code</div><div class="field" style="left:304px;top:2px;width:199px"></div></div>
  <div class="form-row" style="top:308px;height:25px"><div class="form-label req">Country</div>
    <div class="field select" style="left:304px;top:2px;width:199px">Australia<svg width="8" height="5"><path d="M0 0h8L4 5z" fill="#333"/></svg></div></div>
  <div class="form-row" style="top:338px;height:52px"><div class="form-label">Phone</div>
    <span class="mini" style="left:306px;top:3px">Country Code</span>
    <span class="mini" style="left:373px;top:3px">Area Code</span>
    <span class="mini" style="left:457px;top:3px">Phone Number</span>
    <div class="field" style="left:304px;top:17px;width:50px"></div>
    <div class="field" style="left:371px;top:17px;width:79px"></div>
    <div class="field" style="left:455px;top:17px;width:141px"></div>
  </div>
  <div class="form-row" style="top:394px;height:25px"><div class="form-label">Mobile</div><div class="field" style="left:304px;top:2px;width:199px"></div></div>
  <div class="btn-update">Update</div>
</section>

<aside class="panel member">
  <div class="panel-head">Member Option
    <svg width="20" height="16" viewBox="0 0 20 16"><rect width="20" height="16" rx="2" fill="#555"/><path d="M6 6h8l-4 5z" fill="#fff"/></svg>
  </div>
  <ul class="member-list">
    <li>Edit Your Profiles</li><li>Change Password</li><li>My Resumes</li><li>Post Resume</li><li>My Cover Letters</li>
    <li>Add cover Letter</li><li>My Applied Jobs</li><li>My Searches</li><li>Unsubscribe Newsletter</li><li>Log Out</li>
  </ul>
</aside>

<section class="panel employers">
  <div class="panel-head">Featured Employers</div>
  <div class="arrow prev"><svg width="10" height="16"><path d="M9 1L2 8l7 7" fill="none" stroke="#444" stroke-width="3"/></svg></div>
  <div class="employer-track">
    <div class="employer northfield">Northfield</div>
    <div class="employer harborline"><span class="dot"></span>Harborline</div>
    <div class="employer ridgeway">Ridgeway</div>
    <div class="employer greenpoint"><span class="dot"></span>Greenpoint</div>
    <div class="employer summit">Summit</div>
    <div class="employer aztera">Aztera</div>
  </div>
  <div class="arrow next"><svg width="10" height="16"><path d="M1 1l7 7-7 7" fill="none" stroke="#444" stroke-width="3"/></svg></div>
</section>

<nav class="footer-links">
  <span>Home</span><span>|</span><span>About Us</span><span>|</span><span>Search Jobs</span><span>|</span><span>Candidates</span><span>|</span><span>Recruiters</span><span>|</span><span>FAQ's</span><span>|</span><span>Blogs</span><span>|</span><span>Log in</span><span>|</span><span>Register</span><span>|</span><span>Terms of Use</span><span>|</span><span>Privacy Policy</span><span>|</span><span>Contact Us</span>
</nav>
<div class="copyright">Copyright © 2012, Crestlinecareers.com. All rights reserved.</div>
</body>
</html>
```